Business Card And Stationary Set for : Pintu Ravel Sdn. Bhd.
I need double sided standard sized Business Card [3.5" x 2"]
Same font or you can recommend
Professional
Ferril Wakin
41C, Jalan Cempaka Lima,
Taman Seroja,
47310 Kuala Lumpur,
Malaysia.
info@pintuvrel.com.my
www.pintuvrel.com.my
618204-K
Please put the company name and license no. above the company address. Smaller font for the license number.
Pintu Ravel Sdn. Bhd. (618204-K)
Company logo.
Specialized In: Auto Gate & Security Systems

```html
<!DOCTYPE html>
<html lang="en">
<head>
<meta charset="utf-8">
<title>Pintu Ravel Sdn. Bhd. – Stationery Set</title>
<link href="https://fonts.googleapis.com/css2?family=Open+Sans:wght@400;700;800&display=swap" rel="stylesheet">
<style>
:root{
  --orange:#f7931e;
  --orange-deep:#e8731a;
  --charcoal:#2a2a2a;
  --charcoal-soft:#3d3d3d;
  --grey:#8c8c8c;
  --paper:#ffffff;
  --ground:#efeae3;
  --ink:#333333;
  --faint:#ececec;
}
*{box-sizing:border-box;margin:0;padding:0}
html,body{width:1200px;height:418px;overflow:hidden}
body{background:var(--ground);font-family:"Open Sans",Arial,sans-serif;color:var(--ink);position:relative}
.sheet{position:absolute;background:var(--paper);box-shadow:0 2px 5px rgba(0,0,0,.18);overflow:hidden}
.brand{display:flex;align-items:center;gap:4px;font-weight:800;text-transform:uppercase;line-height:1;letter-spacing:.02em;white-space:nowrap}
.brand-square{display:inline-block;background:currentColor;flex:none}
.wedge{position:absolute;background:linear-gradient(135deg,var(--orange),var(--orange-deep))}
.wedge-dark{position:absolute;background:var(--charcoal)}
.fine{font-size:4px;line-height:1.45;color:#555}

/* business cards */
.card{width:144px;height:84px}
.card-front{left:12px;top:29px}
.card-back-dark{left:168px;top:29px;background:var(--charcoal)}
.card-logo-white{left:12px;top:132px}
.card-orange{left:168px;top:132px;background:linear-gradient(135deg,var(--orange),var(--orange-deep))}
.card-dark-solo{left:96px;top:233px;width:151px;height:79px;background:linear-gradient(160deg,var(--charcoal-soft),var(--charcoal))}
.card .card-brand{position:absolute;left:6px;top:44px;font-size:5.5px}
.card .holder{position:absolute;left:66px;top:10px;font-size:6px;font-weight:700;color:var(--orange)}
.card .contact{position:absolute;left:66px;top:20px;width:74px}
.card-back-dark .contact{color:#ccc}
.card-centred{display:flex;flex-direction:column;align-items:center;justify-content:center;gap:4px}
.tagline{font-size:4px;color:#bbb}

/* letterhead */
.letterhead{left:336px;top:19px;width:259px;height:346px}
.letterhead .brand{position:absolute;right:14px;top:12px;font-size:9px;color:var(--charcoal)}
.letterhead-footer{position:absolute;left:10px;width:140px;bottom:8px;text-align:left}
.mark-faint{position:absolute;border:14px solid var(--faint)}
.footer-line{position:absolute;left:0;right:0;bottom:8px;text-align:center}

/* envelopes */
.envelope-grey{left:612px;top:19px;width:288px;height:118px}
.envelope-white{left:612px;top:91px;width:288px;height:130px}
.envelope-orange{left:492px;top:144px;width:312px;height:221px}
.flap{position:absolute;left:0;top:0;width:100%}
.tall{left:907px;top:19px;width:281px;height:370px}
</style>
</head>
<body>

<!-- business card: front -->
<div class="sheet card card-front">
  <div class="wedge" style="left:0;top:0;width:34px;height:34px;clip-path:polygon(0 0,100% 0,0 100%)"></div>
  <div class="brand card-brand" style="color:var(--charcoal)"><span class="brand-square" style="width:5px;height:5px;background:var(--orange)"></span>Pintu Ravel</div>
  <div class="holder">Ferril Wakin</div>
  <div class="contact fine">Director<br>Tel: +603-5512 4470<br>info@pintuvrel.com.my<br>www.pintuvrel.com.my<br>41C, Jalan Cempaka Lima,<br>Taman Seroja, 47310</div>
</div>

<!-- business card: dark variant -->
<div class="sheet card card-back-dark">
  <div class="wedge" style="left:0;top:0;width:34px;height:34px;clip-path:polygon(0 0,100% 0,0 100%)"></div>
  <div class="brand card-brand" style="color:var(--paper)"><span class="brand-square" style="width:5px;height:5px;background:var(--orange)"></span>Pintu Ravel</div>
  <div class="holder">Ferril Wakin</div>
  <div class="contact fine">Director<br>Tel: +603-5512 4470<br>info@pintuvrel.com.my<br>www.pintuvrel.com.my<br>41C, Jalan Cempaka Lima,<br>Taman Seroja, 47310</div>
</div>

<!-- business card: white logo side -->
<div class="sheet card card-logo-white card-centred">
  <div class="wedge" style="right:0;bottom:0;width:22px;height:30px;clip-path:polygon(100% 0,100% 100%,0 100%)"></div>
  <div class="brand" style="font-size:10px;color:var(--charcoal)"><span class="brand-square" style="width:9px;height:9px;background:var(--orange)"></span>Pintu Ravel</div>
</div>

<!-- business card: orange side -->
<div class="sheet card card-orange card-centred">
  <div class="wedge-dark" style="right:0;top:0;width:26px;height:84px;clip-path:polygon(100% 0,100% 100%,60% 100%)"></div>
  <div class="brand" style="font-size:10px;color:var(--paper)"><span class="brand-square" style="width:9px;height:9px"></span>Pintu Ravel</div>
</div>

<!-- business card: dark logo side -->
<div class="sheet card card-dark-solo card-centred">
  <div class="brand" style="font-size:10px;color:var(--paper)"><span class="brand-square" style="width:9px;height:9px;background:var(--orange)"></span>Pintu Ravel</div>
  <div class="tagline">Auto Gate &amp; Security Systems</div>
</div>

<!-- letterhead -->
<div class="sheet letterhead">
  <div class="wedge" style="left:0;top:0;width:14px;height:40px;clip-path:polygon(0 0,100% 0,0 100%)"></div>
  <div class="brand"><span class="brand-square" style="width:9px;height:9px;background:var(--orange)"></span>Pintu Ravel</div>
  <div class="mark-faint" style="left:60px;top:100px;width:120px;height:120px"></div>
  <div class="wedge" style="right:0;bottom:0;width:16px;height:40px;clip-path:polygon(100% 0,100% 100%,0 100%)"></div>
  <div class="letterhead-footer fine">Pintu Ravel Sdn. Bhd. (618204-K)<br>41C, Jalan Cempaka Lima, Taman Seroja, 47310 Kuala Lumpur<br>info@pintuvrel.com.my · www.pintuvrel.com.my</div>
</div>

<!-- envelope: grey flap -->
<div class="sheet envelope-grey">
  <svg class="flap" width="288" height="70" viewBox="0 0 288 70" aria-hidden="true">
    <path d="M0 0H288V18L144 62L0 18Z" fill="#8c8c8c"/>
  </svg>
  <div class="brand" style="position:absolute;left:124px;top:16px;font-size:7px;color:var(--paper)"><span class="brand-square" style="width:7px;height:7px"></span>Pintu Ravel</div>
</div>

<!-- envelope: white back -->
<div class="sheet envelope-white">
  <svg class="flap" width="288" height="60" viewBox="0 0 288 60" aria-hidden="true">
    <path d="M0 0L144 48L288 0" fill="none" stroke="#dcdcdc" stroke-width="1.5"/>
  </svg>
  <div class="mark-faint" style="right:30px;top:40px;width:70px;height:70px;border-width:9px"></div>
</div>

<!-- envelope: orange flap -->
<div class="sheet envelope-orange">
  <svg class="flap" width="312" height="72" viewBox="0 0 312 72" aria-hidden="true">
    <defs><linearGradient id="flapOrange" x1="0" y1="0" x2="1" y2="1"><stop offset="0" stop-color="#f7931e"/><stop offset="1" stop-color="#e8731a"/></linearGradient></defs>
    <path d="M0 0H312V40Q230 10 156 50Q80 10 0 40Z" fill="url(#flapOrange)"/>
  </svg>
  <div class="brand" style="position:absolute;left:138px;top:10px;font-size:7px;color:var(--paper)"><span class="brand-square" style="width:7px;height:7px"></span>Pintu Ravel</div>
  <div class="mark-faint" style="left:170px;top:90px;width:90px;height:90px;border-width:11px"></div>
  <div class="wedge" style="right:0;bottom:0;width:14px;height:34px;clip-path:polygon(100% 0,100% 100%,0 100%)"></div>
  <div class="footer-line fine">Pintu Ravel Sdn. Bhd. (618204-K) · 41C, Jalan Cempaka Lima, Taman Seroja, 47310 Kuala Lumpur</div>
</div>

<!-- tall envelope -->
<div class="sheet tall">
  <svg class="flap" width="281" height="80" viewBox="0 0 281 80" aria-hidden="true">
    <defs><linearGradient id="tallOrange" x1="0" y1="0" x2="1" y2="1"><stop offset="0" stop-color="#f7931e"/><stop offset="1" stop-color="#e8731a"/></linearGradient></defs>
    <path d="M0 0H281V46Q210 14 140 64Q70 14 0 46Z" fill="url(#tallOrange)"/>
  </svg>
  <div class="brand" style="position:absolute;left:112px;top:12px;font-size:8px;color:var(--paper)"><span class="brand-square" style="width:8px;height:8px"></span>Pintu Ravel</div>
  <div class="mark-faint" style="left:40px;top:120px;width:120px;height:120px"></div>
  <div class="wedge" style="right:0;bottom:0;width:16px;height:40px;clip-path:polygon(100% 0,100% 100%,0 100%)"></div>
  <div class="footer-line fine">Pintu Ravel Sdn. Bhd. (618204-K) · 41C, Jalan Cempaka Lima, Taman Seroja, 47310 Kuala Lumpur<br>info@pintuvrel.com.my · www.pintuvrel.com.my</div>
</div>

</body>
</html>
```